New Company Business Card design

Looking for a corporate looking business card utilising my new logo design - the logo i would like embossed as one option and flat as another - simplistic but stylish - less is more - we are an import export business launching into the market - i would like a couple of options as main background - Grey or Black

```html
<!DOCTYPE html>
<html lang="en">
<head>
<meta charset="utf-8">
<title>Meridian Trade Partners – Business Cards</title>
<link rel="stylesheet" href="https://fonts.googleapis.com/css2?family=Lato:wght@400;700&display=swap">
<style>
  :root {
    --stage: #2a2d31;
    --card: #e4e5e7;
    --blue: #1b74c4;
    --blue-deep: #0d57b0;
    --blue-mid: #1565bd;
    --grey: #6d6e70;
    --ink: #1d1d1f;
  }
  * { margin: 0; padding: 0; box-sizing: border-box; }
  html, body { width: 1200px; height: 900px; overflow: hidden; }
  body {
    background: var(--stage);
    font-family: "Lato", Arial, sans-serif;
    position: relative;
  }
  .card {
    position: absolute;
    top: 295px;
    width: 540px;
    height: 310px;
    background: var(--card);
    border-radius: 22px;
    overflow: hidden;
  }
  .card--front { left: 40px; }
  .card--back { left: 620px; }
  .card__band { position: absolute; left: 0; top: 0; width: 540px; height: 310px; }

  .brand { position: absolute; display: flex; align-items: center; gap: 10px; }
  .brand__dot { width: 14px; height: 14px; border-radius: 50%; background: var(--blue); flex: none; }
  .brand__name {
    color: var(--blue);
    font-weight: 700;
    font-size: 15px;
    letter-spacing: 1.5px;
    text-transform: uppercase;
    line-height: 1.25;
    white-space: nowrap;
  }
  .card--front .brand { left: 30px; top: 52px; }
  .card--back .brand { left: 50%; top: 92px; transform: translateX(-50%); }
  .card--back .brand__name { font-size: 20px; letter-spacing: 2px; }

  .divider {
    position: absolute;
    left: 232px; top: 30px;
    width: 2px; height: 186px;
    background: var(--ink);
  }
  .person { position: absolute; left: 250px; top: 32px; }
  .person__name {
    font-size: 18px;
    color: var(--ink);
    font-variant: small-caps;
    letter-spacing: 1px;
  }
  .person__role {
    font-size: 13px;
    color: var(--blue);
    font-variant: small-caps;
    letter-spacing: 1px;
    margin-top: 2px;
  }
  .contacts { position: absolute; left: 250px; top: 96px; list-style: none; }
  .contacts__item {
    display: flex; align-items: flex-start; gap: 9px;
    color: var(--blue);
    font-size: 14px;
    line-height: 1.2;
    margin-bottom: 9px;
    white-space: nowrap;
  }
  .contacts__icon {
    width: 20px; height: 20px; flex: none;
    background: var(--blue);
    border-radius: 3px;
  }
  .website {
    position: absolute;
    left: 0; right: 0; top: 160px;
    text-align: center;
    color: var(--blue);
    font-size: 17px;
    letter-spacing: .3px;
  }
</style>
</head>
<body>

<svg width="0" height="0" style="position:absolute">
  <defs>
    <g id="card-band">
      <path d="M0,178 C28,186 36,232 60,250 C75,262 90,262 110,262 L470,262 C500,262 520,258 540,232 L540,310 L0,310 Z" fill="var(--blue)"/>
      <path d="M52,230 C58,250 72,262 100,262 L150,262 L150,282 L95,282 C70,282 56,262 52,230 Z" fill="var(--grey)"/>
      <rect x="150" y="262" width="112" height="20" fill="var(--blue-deep)"/>
      <rect x="264" y="262" width="114" height="20" fill="var(--blue-mid)"/>
      <path d="M380,262 L500,262 C510,262 515,266 505,282 L380,282 Z" fill="var(--grey)"/>
    </g>
  </defs>
</svg>

<section class="card card--front" aria-label="Business card, contact side">
  <svg class="card__band" viewBox="0 0 540 310" aria-hidden="true"><use href="#card-band"/></svg>

  <div class="brand">
    <span class="brand__dot"></span>
    <span class="brand__name">Meridian Trade<br>Partners</span>
  </div>

  <div class="divider"></div>

  <div class="person">
    <p class="person__name">Daniel R. Marsh</p>
    <p class="person__role">Founder</p>
  </div>

  <ul class="contacts">
    <li class="contacts__item">
      <svg class="contacts__icon" viewBox="0 0 20 20" aria-hidden="true"><path d="M10,3 C7,3 5,5 5,8 C5,11 10,17 10,17 C10,17 15,11 15,8 C15,5 13,3 10,3 Z M10,10 A2,2 0 1 1 10,6 A2,2 0 1 1 10,10 Z" fill="#fff"/></svg>
      <span>482 Harbor Avenue, Portland<br>OR 97204</span>
    </li>
    <li class="contacts__item">
      <svg class="contacts__icon" viewBox="0 0 20 20" aria-hidden="true"><path d="M6,3 L8.5,3 L9.5,7 L8,8.5 C9,10.5 10,11.5 11.5,12.5 L13,11 L17,12 L17,14.5 C17,15.5 16,16.5 15,16.5 C9,16.5 3.5,11 3.5,5 C3.5,4 4.5,3 6,3 Z" fill="#fff"/></svg>
      <span>555-014-2287</span>
    </li>
    <li class="contacts__item">
      <svg class="contacts__icon" viewBox="0 0 20 20" aria-hidden="true"><rect x="4" y="8" width="12" height="8" fill="#fff"/><rect x="6" y="3" width="8" height="5" fill="none" stroke="#fff" stroke-width="1.4"/><rect x="6" y="10" width="8" height="1.4" fill="var(--blue)"/></svg>
      <span>555-019-3370</span>
    </li>
    <li class="contacts__item">
      <svg class="contacts__icon" viewBox="0 0 20 20" aria-hidden="true"><rect x="3.5" y="5.5" width="13" height="9" fill="none" stroke="#fff" stroke-width="1.4"/><path d="M3.5,5.5 L10,11 L16.5,5.5" fill="none" stroke="#fff" stroke-width="1.4"/></svg>
      <span>dmarsh@meridiantrade.com</span>
    </li>
  </ul>
</section>

<section class="card card--back" aria-label="Business card, brand side">
  <svg class="card__band" viewBox="0 0 540 310" aria-hidden="true"><use href="#card-band"/></svg>

  <div class="brand">
    <span class="brand__dot"></span>
    <span class="brand__name">Meridian Trade<br>Partners</span>
  </div>

  <p class="website">www.meridiantrade.com</p>
</section>

</body>
</html>
```